Door Hanger Design for Electricians Serving Homes

I would like our logo incorporated into the door hanger. We would like a place for a tear off section on the bottom of the hanger with our contact information: K&T Electric - (555) 318-6470 - www.kandtelectric.example - info@kandtelectric.example.
Door Hanger Script
Front Side of the Door Hanger:
[Company Logo]
Need a Reliable Electrician?
Your Local Electrical Expert is Just Around the Corner!
• Quick Response Times
• Affordable Rates
• Quality Workmanship
• Fully Licensed & Insured
• Special Offer:
• 10% OFF Your First Service Call!
Back Side of the Door Hanger:
Don't Let Electrical Issues Keep You in the Dark!
From flickering lights to complete system upgrades, we've got all your
residential electrical needs covered. Our services include:
• Electrical Repairs & Troubleshooting
• Lighting Installation & Upgrades
• Safety Inspections & Code Compliance
• Energy-Efficient Solutions
• 24/7 Emergency Services
• Why Choose Us?
• Friendly, Local Service
• Over 30 Years of Experience
• Satisfaction Guaranteed
• Upfront Pricing
Call Us Today: [Your Phone Number]
Visit Our Website: [Your Website]
Book Your Appointment Now and Claim Your 10% Discount!
Offer valid for new customers on the first visit only. Mention this door hanger when
booking.
[Your Company Name and Contact Information]
Follow Us on Social Media for More Tips and Special Offers!
[Icons for social media platforms: Chatterbook, Snapwave, Peeper, etc.]
Design Tips:
Use bold, clear fonts for easy reading.
Incorporate your brand colors and logo for instant recognition.
Include a clear call to action (CTA) on both sides.
Add a tear-off section at the bottom with your contact information for
convenience.
Use high-quality images or graphics related to electrical work to catch
the eye.
This door hanger design and copy aim to attract residential clients by
highlighting the benefits of your electrical services, special offers, and
how they can easily get in touch with you for their electrical needs.
The door knocker template will have three of the same design on front and three of the same design on the back. This template is from the print shop.

```html
<!DOCTYPE html>
<html lang="en">
<head>
<meta charset="utf-8">
<title>K&amp;T Electric Door Hanger</title>
<link href="https://fonts.googleapis.com/css2?family=Anton&family=Bebas+Neue&family=Montserrat:wght@400;900&family=Pathway+Gothic+One&family=Roboto:ital,wght@0,400;1,900&family=Oswald:wght@600&display=swap" rel="stylesheet">
<style>
  :root {
    --red: #c92b2b;
    --red-light: #d8443f;
    --red-deep: #b02222;
    --white: #ffffff;
    --ink: #111111;
    --bar: #2e2e2e;
    --accent: #e31e24;
  }
  * { margin: 0; padding: 0; box-sizing: border-box; }
  html, body { width: 846px; height: 1200px; overflow: hidden; background: var(--white); }
  .hanger { position: relative; width: 846px; height: 1200px; overflow: hidden; background: var(--white); }
  .panel {
    position: absolute; left: 0; top: 0; width: 846px; height: 1125px;
    background:
      radial-gradient(circle at 20% 30%, var(--red-light) 0, transparent 35%),
      radial-gradient(circle at 80% 60%, var(--red-light) 0, transparent 30%),
      linear-gradient(180deg, var(--red) 0%, var(--red-deep) 100%);
  }
  .scallop { position: absolute; left: 0; top: 0; }
  .hole-slot { position: absolute; left: 404px; top: 0; width: 38px; height: 40px; background: var(--white); }
  .hole { position: absolute; left: 336px; top: 24px; width: 174px; height: 174px; border-radius: 50%; background: var(--white); }
  .brand {
    position: absolute; left: 17px; top: 39px; width: 149px; height: 124px;
    background: var(--white); display: flex; align-items: center; justify-content: center;
    box-shadow: 2px 3px 4px rgba(0,0,0,.35);
    font-family: "Oswald", sans-serif; font-weight: 600; font-size: 24px; color: var(--ink);
    text-align: center; line-height: 1.05;
  }
  .headline {
    position: absolute; left: 0; width: 846px; text-align: center;
    font-family: "Anton", sans-serif; font-style: italic; color: var(--white);
    text-shadow: 2px 3px 3px rgba(0,0,0,.35); line-height: 1; letter-spacing: -1px;
    font-size: 75px; white-space: nowrap;
  }
  .headline--one { top: 201px; }
  .headline--two { top: 277px; }
  .headline .dark { color: var(--ink); }
  .intro {
    position: absolute; left: 32px; top: 373px; width: 781px; height: 62px;
    background: var(--white); border-radius: 3px;
    font-family: "Montserrat", sans-serif; font-size: 27px; color: var(--red);
    line-height: 27px; padding: 3px 0 0 8px; white-space: nowrap; letter-spacing: .5px;
  }
  .col-title {
    position: absolute; top: 467px; height: 28px; background: var(--ink); border-radius: 3px;
    font-family: "Roboto", sans-serif; font-style: italic; font-weight: 900; font-size: 26px;
    color: var(--white); line-height: 28px; text-align: center;
  }
  .col-title--services { left: 77px; width: 278px; }
  .col-title--why { left: 480px; width: 278px; }
  .worker {
    position: absolute; left: 600px; top: 690px; width: 246px; height: 435px;
    background: linear-gradient(180deg, #e8863a 0%, #c94c3e 22%, #3559b0 55%, #2a2a2a 85%, #3559b0 100%);
    border-radius: 110px 0 0 0; opacity: .9;
  }
  .list { position: absolute; list-style: none; }
  .list--services { left: 22px; top: 500px; width: 388px; }
  .list--why { left: 434px; top: 503px; width: 387px; }
  .list li {
    position: relative; height: 40px; margin-bottom: 5.5px; background: var(--bar);
    border-radius: 3px; box-shadow: 1px 3px 4px rgba(0,0,0,.35);
    font-family: "Roboto", sans-serif; font-size: 20.5px; color: var(--white);
    line-height: 38px; padding-left: 29px; white-space: nowrap;
  }
  .list li svg { position: absolute; left: 6px; top: 10px; }
  .cta {
    position: absolute; left: 27px; top: 748px;
    font-family: "Bebas Neue", sans-serif; font-size: 57px; line-height: 52px; color: var(--white);
    letter-spacing: .5px; white-space: nowrap;
  }
  .coupon {
    position: absolute; left: 28px; top: 863px; width: 333px; height: 113px;
    background: linear-gradient(135deg, #ffffff 0%, #eaeaea 60%, #d6d6d6 100%);
    border-radius: 12px; text-align: center;
  }
  .coupon-fold { position: absolute; right: 0; top: 0; }
  .coupon-rate { font-family: "Montserrat", sans-serif; font-weight: 900; font-size: 58px; color: var(--accent); line-height: 52px; padding-top: 9px; padding-right: 14px; letter-spacing: -1px; }
  .coupon-label { font-family: "Montserrat", sans-serif; font-weight: 900; font-size: 45px; color: var(--ink); line-height: 44px; padding-right: 14px; }
  .terms {
    position: absolute; left: 27px; top: 985px;
    font-family: "Pathway Gothic One", sans-serif; font-size: 38px; line-height: 38px; color: var(--white);
    white-space: nowrap;
  }
  .social { position: absolute; left: 30px; top: 1096px; display: flex; align-items: center; gap: 10px; }
  .social-dot { width: 20px; height: 20px; border-radius: 50%; background: var(--white); }
  .social-handle { font-family: "Montserrat", sans-serif; font-size: 19px; letter-spacing: 3px; color: var(--white); }
  .tear { position: absolute; left: 0; top: 1125px; width: 846px; height: 75px; }
  .tear-web, .tear-mail, .tear-phone { position: absolute; white-space: nowrap; }
  .tear-web, .tear-mail {
    top: 29px; font-family: "Montserrat", sans-serif; font-size: 15px; letter-spacing: 1.5px; color: var(--ink);
  }
  .tear-web { left: 16px; }
  .tear-mail { left: 318px; }
  .tear-phone {
    right: 12px; top: 12px; font-family: "Oswald", sans-serif; font-weight: 600; font-size: 36px;
    line-height: 48px; color: var(--accent); letter-spacing: -1px;
  }
</style>
</head>
<body>
<div class="hanger">
  <div class="panel"></div>
  <svg class="scallop" width="846" height="16" viewBox="0 0 846 16" aria-hidden="true">
    <defs>
      <pattern id="wave" width="26" height="16" patternUnits="userSpaceOnUse">
        <path d="M0 0 H26 V2 Q13 18 0 2 Z" fill="#ffffff"/>
      </pattern>
    </defs>
    <rect width="846" height="16" fill="url(#wave)"/>
  </svg>
  <div class="hole-slot"></div>
  <div class="hole"></div>

  <div class="brand">K&amp;T<br>Electric</div>

  <h1 class="headline headline--one">DON'T LET ELECTRICAL ISSUES</h1>
  <h1 class="headline headline--two">KEEP YOU IN THE <span class="dark">DARK!</span></h1>

  <p class="intro">From flickering lights to complete system upgrades,<br>we've got all your residential electrical needs covered.</p>

  <div class="worker" role="img" aria-label="Photo of a smiling electrician in an orange hard hat, red shirt and blue overalls, holding a clipboard with a tool belt"></div>

  <h2 class="col-title col-title--services">Our Service Include</h2>
  <ul class="list list--services">
    <li><svg width="14" height="20" viewBox="0 0 14 20"><path d="M2 2 L11 10 L2 18" stroke="#000" stroke-width="4" fill="none"/></svg>Electrical Repairs &amp; Troubleshooting</li>
    <li><svg width="14" height="20" viewBox="0 0 14 20"><path d="M2 2 L11 10 L2 18" stroke="#000" stroke-width="4" fill="none"/></svg>Lighting Installation &amp; Upgrades</li>
    <li><svg width="14" height="20" viewBox="0 0 14 20"><path d="M2 2 L11 10 L2 18" stroke="#000" stroke-width="4" fill="none"/></svg>Safety Inspections &amp; Code Compliance</li>
    <li><svg width="14" height="20" viewBox="0 0 14 20"><path d="M2 2 L11 10 L2 18" stroke="#000" stroke-width="4" fill="none"/></svg>Energy-Efficient Solutions</li>
    <li><svg width="14" height="20" viewBox="0 0 14 20"><path d="M2 2 L11 10 L2 18" stroke="#000" stroke-width="4" fill="none"/></svg>24/7 Emergency Services</li>
  </ul>

  <h2 class="col-title col-title--why">Why Choose Us?</h2>
  <ul class="list list--why">
    <li><svg width="14" height="20" viewBox="0 0 14 20"><path d="M2 2 L11 10 L2 18" stroke="#000" stroke-width="4" fill="none"/></svg>Friendly, Local Service</li>
    <li><svg width="14" height="20" viewBox="0 0 14 20"><path d="M2 2 L11 10 L2 18" stroke="#000" stroke-width="4" fill="none"/></svg>Over 30 Years of Experience</li>
    <li><svg width="14" height="20" viewBox="0 0 14 20"><path d="M2 2 L11 10 L2 18" stroke="#000" stroke-width="4" fill="none"/></svg>Satisfaction Guaranteed</li>
    <li><svg width="14" height="20" viewBox="0 0 14 20"><path d="M2 2 L11 10 L2 18" stroke="#000" stroke-width="4" fill="none"/></svg>Upfront Pricing</li>
  </ul>

  <p class="cta">BOOK YOUR APPOINTMENT<br>NOW AND CLAIM YOUR</p>

  <div class="coupon">
    <svg class="coupon-fold" width="38" height="38" viewBox="0 0 38 38" aria-hidden="true">
      <path d="M0 0 H38 V38 Z" fill="#c92b2b"/>
      <path d="M0 0 Q8 30 38 38 Q12 38 0 0 Z" fill="#bdbdbd"/>
    </svg>
    <div class="coupon-rate">10%</div>
    <div class="coupon-label">DISCOUNT</div>
  </div>

  <p class="terms">Offer valid for new customers on the first visit only.<br>Mention this door hanger when booking.</p>

  <div class="social">
    <span class="social-dot"></span>
    <span class="social-handle">kandtelectric</span>
  </div>

  <footer class="tear">
    <span class="tear-web">www.kandtelectric.example</span>
    <span class="tear-mail">info@kandtelectric.example</span>
    <span class="tear-phone">(555) 318-6470</span>
  </footer>
</div>
</body>
</html>
```